Introduction Post card

Harbourline Doors
42 Kestrel Lane
Ruthven Ontario
Ned@harbourlinedoors.example
519-555-0147

Dear Leamington Residents

We are excited to announce the launch of Harbourline Doors, your new local source for high-quality windows, doors, and garage doors! As a dedicated member of this community, we are committed to providing exceptional products and services that enhance the beauty and functionality of your home or business.

At Harbourline Doors, we understand that choosing the right windows and doors is essential for energy efficiency, security, and style. That’s why we offer a wide selection of premium products tailored to meet your unique needs. Our expert team is here to guide you through the selection process, ensuring you find the perfect fit for your space.

Our services don’t stop at providing quality products. We pride ourselves on our professional installation process, ensuring that every project is completed with precision and care. Customer satisfaction is our top priority, and we strive to exceed your expectations with every interaction.

We invite you to visit our showroom or contact us to learn more about our offerings. Whether you’re looking to upgrade your home’s curb appeal or enhance its security, we are here to help. Together, let’s make our community a more beautiful place!

Thank you for considering Harbourline Doors for your window, door, and garage door needs. We look forward to serving you!

Warm regards,

Ned
Sales Manager
Harbourline Doors
https://harbourlinedoors.example/

```html
<!DOCTYPE html>
<html lang="en">
<head>
<meta charset="utf-8">
<title>Harbourline Doors – Introduction Postcard</title>
<link href="https://fonts.googleapis.com/css2?family=Fira+Sans+Condensed:wght@600;700&family=Figtree:wght@400;500&family=Outfit:wght@400;500&family=Great+Vibes&display=swap" rel="stylesheet">
<style>
  :root{
    --stage:#a7a7a7;
    --paper:#ffffff;
    --ink:#2e2e2e;
    --body:#3b3b3b;
    --orange:#e8582a;
    --charcoal:#2a2a28;
    --back:#302f2b;
    --white:#ffffff;
  }
  *{margin:0;padding:0;box-sizing:border-box}
  html,body{width:1200px;height:1200px;overflow:hidden;background:var(--stage)}
  .stage{position:relative;width:1200px;height:1200px}

  /* Front */
  .card-front{position:absolute;left:83px;top:81px;width:700px;height:507px;background:var(--paper);overflow:hidden}
  .sky{position:absolute;left:176px;top:210px;right:0;height:110px;
       background:linear-gradient(180deg,rgba(255,255,255,0) 0%,#f3d6dc 55%,#e9a6b1 100%)}
  .house-photo{position:absolute;left:0;right:0;top:298px;bottom:0;
       background:linear-gradient(180deg,#7d7b7e 0%,#5a5452 35%,#4a3b30 70%,#3a3f2c 100%)}
  .sidebar{position:absolute;left:0;top:0;width:176px;height:298px;background:var(--paper);text-align:center}
  .brand-mark{display:flex;justify-content:center;align-items:center;gap:6px;margin-top:64px}
  .brand-square{width:10px;height:10px;background:var(--orange)}
  .brand-name{font-family:"Fira Sans Condensed",sans-serif;font-weight:700;font-size:17px;color:var(--orange);letter-spacing:.2px}
  .portrait{position:absolute;left:51px;top:114px;width:74px;height:74px;border-radius:50%;
       border:1.5px solid var(--orange);background:radial-gradient(circle at 50% 40%,#8c8e90,#44474a)}
  .rep-name{position:absolute;left:0;right:0;top:193px;font-family:"Outfit",sans-serif;font-weight:500;font-size:15px;color:var(--ink)}
  .rep-title{position:absolute;left:0;right:0;top:212px;font-family:"Outfit",sans-serif;font-size:8.5px;color:var(--orange)}
  .rep-phone{position:absolute;left:45px;top:230px;width:86px;height:14px;border-radius:7px;background:var(--orange);
       color:var(--white);font-family:"Outfit",sans-serif;font-size:8.5px;line-height:14px;display:flex;justify-content:center;align-items:center;gap:3px}
  .rep-contact{position:absolute;left:0;right:0;top:250px;font-family:"Outfit",sans-serif;font-size:8.5px;line-height:11px;color:var(--ink)}

  .letter{position:absolute;left:203px;top:28px;width:480px;color:var(--body)}
  .greeting{font-family:"Figtree",sans-serif;font-weight:500;font-size:19px;color:var(--ink);margin-bottom:11px}
  .greeting span{color:var(--orange)}
  .letter p{font-family:"Figtree",sans-serif;font-size:8.6px;line-height:10.6px;margin-bottom:6.5px}
  .letter p.closing{font-weight:500;font-size:10.4px;line-height:13.5px;color:#111;margin-top:8px}
  .signoff{font-family:"Great Vibes",cursive;font-size:22px;color:var(--ink);margin-top:10px}

  .info-bar{position:absolute;left:39px;width:620px;bottom:0;height:40px;background:var(--charcoal);
       border:1px solid var(--orange);border-bottom:none;border-radius:26px 26px 0 0;
       display:flex;align-items:center;justify-content:center;gap:18px;
       font-family:"Outfit",sans-serif;font-size:13px;color:var(--white)}
  .info-item{display:flex;align-items:center;gap:5px}
  .info-divider{width:1px;height:22px;background:var(--white)}

  /* Back */
  .card-back{position:absolute;left:404px;top:625px;width:691px;height:501px;background:var(--back)}
  .back-brand{position:absolute;left:0;right:0;top:176px;display:flex;flex-direction:column;align-items:center;gap:20px}
  .back-square{width:36px;height:36px;background:var(--white)}
  .back-name{font-family:"Fira Sans Condensed",sans-serif;font-weight:700;font-size:32px;color:var(--white);letter-spacing:.3px}
  .back-web{position:absolute;left:0;right:0;top:410px;display:flex;justify-content:center;align-items:center;gap:8px;
       font-family:"Outfit",sans-serif;font-size:13px;letter-spacing:.48em;color:var(--white)}
</style>
</head>
<body>
<div class="stage">

  <section class="card-front">
    <div class="sky"></div>
    <div class="house-photo" role="img" aria-label="Photograph of a large stone house with lit windows and three wooden garage doors at dusk"></div>

    <aside class="sidebar">
      <div class="brand-mark"><span class="brand-square"></span><span class="brand-name">HARBOURLINE DOORS</span></div>
      <div class="portrait" role="img" aria-label="Portrait photo of the sales manager"></div>
      <div class="rep-name">Ned Hollis</div>
      <div class="rep-title">Sales Manager</div>
      <div class="rep-phone">
        <svg width="7" height="7" viewBox="0 0 24 24"><path fill="#fff" d="M6.6 10.8a15.1 15.1 0 0 0 6.6 6.6l2.2-2.2a1 1 0 0 1 1-.25 11.4 11.4 0 0 0 3.6.57 1 1 0 0 1 1 1V20a1 1 0 0 1-1 1A17 17 0 0 1 3 4a1 1 0 0 1 1-1h3.5a1 1 0 0 1 1 1c0 1.25.2 2.45.57 3.57a1 1 0 0 1-.25 1z"/></svg>
        519-555-0147
      </div>
      <div class="rep-contact">Ned@harbourlinedoors.example<br>www.harbourlinedoors.example</div>
    </aside>

    <article class="letter">
      <h1 class="greeting">Dear <span>Leamington Residents</span></h1>
      <p>We are excited to announce the launch of Harbourline Doors, your new local source for high-quality windows, doors, and garage doors! As a dedicated member of this community, we are committed to providing exceptional products and services that enhance the beauty and functionality of your home or business.</p>
      <p>At Harbourline Doors, we understand that choosing the right windows and doors is essential for energy efficiency, security, and style. That’s why we offer a wide selection of premium products tailored to meet your unique needs. Our expert team is here to guide you through the selection process, ensuring you find the perfect fit for your space.</p>
      <p>Our services don’t stop at providing quality products. We pride ourselves on our professional installation process, ensuring that every project is completed with precision and care. Customer satisfaction is our top priority, and we strive to exceed your expectations with every interaction.</p>
      <p>We invite you to visit our showroom or contact us to learn more about our offerings. Whether you’re looking to upgrade your home’s curb appeal or enhance its security, we are here to help. Together, let’s make our community a more beautiful place!</p>
      <p class="closing">Thank you for considering Harbourline Doors for your window, door, and garage door needs.<br>We look forward to serving you!</p>
      <div class="signoff">Warm regards,</div>
    </article>

    <footer class="info-bar">
      <span class="info-item">
        <svg width="11" height="13" viewBox="0 0 24 28"><path fill="none" stroke="#e8582a" stroke-width="3" d="M12 26s9-9.5 9-15a9 9 0 0 0-18 0c0 5.5 9 15 9 15z"/><circle cx="12" cy="11" r="3.2" fill="#e8582a"/></svg>
        42 Kestrel Lane Ruthven Ontario
      </span>
      <span class="info-divider"></span>
      <span class="info-item">
        <svg width="11" height="11" viewBox="0 0 24 24"><path fill="#e8582a" d="M6.6 10.8a15.1 15.1 0 0 0 6.6 6.6l2.2-2.2a1 1 0 0 1 1-.25 11.4 11.4 0 0 0 3.6.57 1 1 0 0 1 1 1V20a1 1 0 0 1-1 1A17 17 0 0 1 3 4a1 1 0 0 1 1-1h3.5a1 1 0 0 1 1 1c0 1.25.2 2.45.57 3.57a1 1 0 0 1-.25 1z"/></svg>
        519-555-0147
      </span>
      <span class="info-divider"></span>
      <span class="info-item">
        <svg width="13" height="13" viewBox="0 0 24 24" fill="none" stroke="#e8582a" stroke-width="1.6"><circle cx="12" cy="12" r="10"/><ellipse cx="12" cy="12" rx="4.5" ry="10"/><path d="M2 12h20M4 7h16M4 17h16"/></svg>
        www.harbourlinedoors.example
      </span>
    </footer>
  </section>

  <section class="card-back">
    <div class="back-brand">
      <span class="back-square"></span>
      <span class="back-name">HARBOURLINE DOORS</span>
    </div>
    <div class="back-web">
      <svg width="14" height="14" viewBox="0 0 24 24" fill="none" stroke="#e8582a" stroke-width="1.6"><circle cx="12" cy="12" r="10"/><ellipse cx="12" cy="12" rx="4.5" ry="10"/><path d="M2 12h20M4 7h16M4 17h16"/></svg>
      WWW.HARBOURLINEDOORS.EXAMPLE
    </div>
  </section>

</div>
</body>
</html>
```